Poly Bag Packaging Motorcycle Cables - Veronzo Brand

Poly Bag Dimensions: 33cm(H) x 24cm(W)
We would like to design a genuine Poly Bag Packaging for motorcycle cables.
Veronzo, is one of the leading companies for manufacturing Motorcycles, located in Egypt. Our company is offering high-quality products, the best in the local market, with very competitive prices.
We have a limited time to get this project done, So we Highly appreciate receiving your designs ASAP.
Target Market(s)
Motorcycle Spare parts Buyers
Font styles to use
Colors
Designer to choose colors to be used in the design.
Look and feel
Each slider illustrates characteristics of the customer's brand and the style your logo design should communicate.

```html
<!DOCTYPE html>
<html lang="en">
<head>
<meta charset="utf-8">
<title>Veronzo Motorcycle Cables – Poly Bag Front</title>
<link rel="stylesheet" href="https://fonts.googleapis.com/css2?family=Oswald:wght@200;300;400;700&family=Lato:wght@400&display=swap">
<style>
  :root {
    --stage: #d6d6d6;
    --bag-black: #0b0b0b;
    --bag-glow: #1c1c1c;
    --silver-light: #f2f2f2;
    --silver-mid: #b9b9b9;
    --silver-dark: #6f6f6f;
    --mark-fill: #3a3a3a;
    --label-grey: #c9c9c9;
    --icon-grey: #b3b3b3;
    --strip: #1f1f1f;
    --gold: #d9a520;
    --gold-deep: #8a6410;
  }
  * { box-sizing: border-box; margin: 0; padding: 0; }
  html, body { width: 1200px; height: 642px; overflow: hidden; }
  body {
    background: var(--stage);
    display: flex;
    justify-content: center;
    align-items: center;
  }
  .bag-front {
    position: relative;
    width: 466px;
    height: 642px;
    background: var(--bag-black);
    overflow: hidden;
    font-family: "Oswald", sans-serif;
    color: var(--silver-light);
  }
  .bag-front__backdrop {
    position: absolute;
    inset: 0;
    background: radial-gradient(ellipse at 50% 35%, var(--bag-glow) 0%, var(--bag-black) 70%);
  }
  .brand {
    position: absolute;
    top: 32px;
    left: 0;
    right: 0;
    display: flex;
    flex-direction: column;
    align-items: center;
    gap: 22px;
  }
  .brand__mark {
    width: 150px;
    height: 150px;
    border-radius: 50%;
    background: var(--mark-fill);
  }
  .brand__name {
    font-weight: 400;
    font-size: 36px;
    letter-spacing: 4px;
    text-transform: uppercase;
    color: var(--silver-mid);
    line-height: 1;
  }
  .headline {
    position: absolute;
    top: 288px;
    left: 0;
    right: 0;
    text-align: center;
    line-height: 1;
  }
  .headline__top {
    display: block;
    font-weight: 200;
    font-size: 62px;
    color: var(--silver-mid);
    letter-spacing: -1px;
  }
  .headline__main {
    display: block;
    margin-top: 2px;
    font-weight: 700;
    font-size: 94px;
    letter-spacing: 0;
    background: linear-gradient(180deg, var(--silver-light) 0%, var(--silver-mid) 45%, var(--silver-dark) 100%);
    -webkit-background-clip: text;
    background-clip: text;
    color: transparent;
  }
  .tagline {
    position: absolute;
    top: 452px;
    left: 0;
    right: 0;
    text-align: center;
    font-weight: 300;
    font-size: 24px;
    color: var(--silver-light);
  }
  .benefits {
    position: absolute;
    top: 524px;
    left: 24px;
    display: flex;
    gap: 14px;
    list-style: none;
  }
  .benefit {
    width: 76px;
    display: flex;
    flex-direction: column;
    align-items: center;
    gap: 6px;
  }
  .benefit svg { width: 42px; height: 42px; }
  .benefit__label {
    font-family: "Lato", sans-serif;
    font-size: 9.5px;
    line-height: 1.35;
    text-align: center;
    color: var(--label-grey);
    letter-spacing: .3px;
  }
  .seals {
    position: absolute;
    top: 518px;
    left: 292px;
    width: 190px;
    height: 80px;
    border-radius: 40px 0 0 40px;
    background: var(--strip);
    display: flex;
    align-items: center;
    gap: 14px;
    padding-left: 10px;
  }
  .seal {
    width: 62px;
    height: 62px;
    border-radius: 50%;
    background: var(--gold);
    border: 3px solid var(--gold-deep);
  }
</style>
</head>
<body>
  <main class="bag-front">
    <div class="bag-front__backdrop" role="img" aria-label="Dark decorative backdrop behind the packaging text"></div>

    <header class="brand">
      <div class="brand__mark"></div>
      <span class="brand__name">Veronzo</span>
    </header>

    <h1 class="headline">
      <span class="headline__top">MOTORCYCLE</span>
      <span class="headline__main">CABLES</span>
    </h1>

    <p class="tagline">A sensitive part of the motorcycle</p>

    <ul class="benefits">
      <li class="benefit">
        <svg viewBox="0 0 40 40" fill="none" stroke="var(--icon-grey)" stroke-width="2">
          <circle cx="20" cy="15" r="11"/>
          <path d="M13 24 L9 37 L14 34 L17 38 L20 27 M27 24 L31 37 L26 34 L23 38 L20 27"/>
          <path d="M15 16 h3 v6 h-3 z M18 16 l3 -5 q2 0 1 3 h3 v6 h-7" fill="var(--icon-grey)" stroke="none"/>
        </svg>
        <span class="benefit__label">HIGH-QUALITY<br>PRODUCTS</span>
      </li>
      <li class="benefit">
        <svg viewBox="0 0 40 40" fill="var(--icon-grey)">
          <path d="M12 12 h16 l4 5 -12 13 -12 -13 z"/>
          <path d="M2 22 l6 -2 8 10 v8 h-6 z M38 22 l-6 -2 -8 10 v8 h6 z"/>
          <path d="M20 2 v5 M12 4 l2 4 M28 4 l-2 4" stroke="var(--icon-grey)" stroke-width="2"/>
        </svg>
        <span class="benefit__label">BEST IN THE<br>LOCAL MARKET</span>
      </li>
      <li class="benefit">
        <svg viewBox="0 0 40 40" fill="none" stroke="var(--icon-grey)" stroke-width="2">
          <circle cx="20" cy="20" r="17"/>
          <circle cx="20" cy="20" r="9" fill="var(--icon-grey)"/>
          <path d="M23 16 q-3 -2 -5 0 q-1 2 2 3 q3 1 2 3 q-2 2 -5 0 M20 13 v14" stroke="var(--bag-black)" stroke-width="1.6"/>
        </svg>
        <span class="benefit__label">COMPETITIVE<br>PRICES</span>
      </li>
    </ul>

    <div class="seals">
      <div class="seal"></div>
      <div class="seal"></div>
    </div>
  </main>
</body>
</html>
```